Business Cards/Letterhead for Electrical Contractor
Electrical Contractor
Business Cards/Letterhead for Electrical Contractor - Construction
Creative Brief
Use same font as used in my logo
A combination may be used
Modern
Derek Stallworth
President
48306 Calloway Avenue Westminster, Colorado 80234
derek@quorvantpower.example

```html
<!DOCTYPE html>
<html lang="en">
<head>
<meta charset="utf-8">
<title>Quorvant Power Inc – Business Card</title>
<link rel="stylesheet" href="https://fonts.googleapis.com/css2?family=Exo+2:wght@400;500;600;700&display=swap">
<style>
  :root {
    --backdrop: #2c2e32;
    --card: #ffffff;
    --blue: #3b8ad9;
    --ink: #3a3d42;
    --muted: #55595f;
  }
  * { margin: 0; padding: 0; box-sizing: border-box; }
  html, body { width: 1200px; height: 816px; overflow: hidden; }
  body {
    background: var(--backdrop);
    font-family: "Exo 2", sans-serif;
    position: relative;
  }
  .card {
    position: absolute;
    left: 100px; top: 118px;
    width: 1000px; height: 580px;
    background: var(--card);
    border-radius: 30px;
    overflow: hidden;
  }
  .card__frame { position: absolute; inset: 0; }

  .identity { position: absolute; left: 70px; top: 150px; width: 440px; }
  .identity__head { display: flex; align-items: center; gap: 18px; }
  .identity__name {
    color: var(--blue);
    font-size: 28px; font-weight: 500;
    letter-spacing: 2px; text-transform: uppercase;
    line-height: 1.15;
  }
  .identity__title {
    color: var(--ink);
    font-size: 22px; font-weight: 400;
    letter-spacing: 1px; line-height: 1.2;
  }
  .identity__rule {
    height: 5px; background: var(--blue);
    margin-top: 14px; width: 440px;
  }

  .contact { position: absolute; left: 70px; top: 290px; list-style: none; }
  .contact__row {
    display: flex; align-items: center; gap: 22px;
    margin-bottom: 22px;
    color: var(--muted);
    font-size: 19px; line-height: 1.3; letter-spacing: 1px;
  }
  .contact__icon {
    width: 40px; height: 40px; flex: none;
    border-radius: 50%; background: var(--blue);
    display: flex; align-items: center; justify-content: center;
  }
  .contact__icon svg { width: 22px; height: 22px; fill: #fff; }

  .brand {
    position: absolute;
    left: 870px; top: 290px;
    transform: translate(-50%, -50%) rotate(-90deg);
    display: flex; align-items: center; gap: 16px;
    white-space: nowrap;
  }
  .brand__mark {
    width: 48px; height: 48px; border-radius: 8px;
    background: var(--blue);
  }
  .brand__name {
    color: var(--blue);
    font-size: 34px; font-weight: 600;
    letter-spacing: 3px; text-transform: uppercase;
  }
</style>
</head>
<body>
  <article class="card">
    <svg class="card__frame" width="1000" height="580" viewBox="0 0 1000 580">
      <polyline points="630,-10 630,100 740,210 740,370 630,480 630,590"
                fill="none" stroke="var(--blue)" stroke-width="26" stroke-linejoin="miter"/>
      <polyline points="604,-10 604,110 710,216 710,364 604,470 604,590"
                fill="none" stroke="var(--blue)" stroke-width="3"/>
    </svg>

    <div class="identity">
      <div class="identity__head">
        <span class="contact__icon">
          <svg viewBox="0 0 24 24"><circle cx="12" cy="8" r="4.5"/><path d="M3 22c0-5 4-8 9-8s9 3 9 8z"/></svg>
        </span>
        <div>
          <p class="identity__name">Derek Stallworth</p>
          <p class="identity__title">President</p>
        </div>
      </div>
      <div class="identity__rule"></div>
    </div>

    <ul class="contact">
      <li class="contact__row">
        <span class="contact__icon">
          <svg viewBox="0 0 24 24"><path d="M7 2h10a2 2 0 0 1 2 2v16a2 2 0 0 1-2 2H7a2 2 0 0 1-2-2V4a2 2 0 0 1 2-2zm0 3v13h10V5zm5 14.2a1 1 0 1 0 0 .1z"/></svg>
        </span>
        <span>303 555 0147<br>303 555 0182</span>
      </li>
      <li class="contact__row">
        <span class="contact__icon">
          <svg viewBox="0 0 24 24"><path d="M3 4h18v13H3zm2 2v9h14V6zM8 19h8v2H8z"/></svg>
        </span>
        <span>derek@quorvantpower.example<br>quorvantpower.example</span>
      </li>
      <li class="contact__row">
        <span class="contact__icon">
          <svg viewBox="0 0 24 24"><path d="M12 2a7 7 0 0 1 7 7c0 5-7 13-7 13S5 14 5 9a7 7 0 0 1 7-7zm0 4.5a2.5 2.5 0 1 0 0 5 2.5 2.5 0 0 0 0-5z"/></svg>
        </span>
        <span>48306 Calloway Avenue<br>Westminster CO</span>
      </li>
    </ul>

    <div class="brand">
      <span class="brand__mark"></span>
      <span class="brand__name">Quorvant Power Inc</span>
    </div>
  </article>
</body>
</html>
```